Realtor Business Card for Marisol!

I sell real estate in a tropical location near the ocean, beaches and palm trees.

The homes are higher end, luxury. I want a card that is professional and attention-grabbing. In a sea full of competition, I need to stand out! I don't want the run-of-the mill card that looks like everyone else's with a different name. I want people to say "wow!".
Updates

Project Deadline Extended Reason: I have a little more time that originally anticipated. Added Friday, July 7, 2017

Target Market(s)

All.

Industry/Entity Type

Real Estate Agent

Contact Information for Business Card

Name: Marisol Vankeer-Odham
Email: marisol@harborview-estates.example
Website: www.harborviewestates.example
Phone: 555.418.7263

Font styles to use
Serif

Colors

Designer to choose colors to be used in the design.

Requirements
Must have
• All attachments.
Nice to have
• Gold edges
• Transparent card
• Unique shape

```html
<!DOCTYPE html>
<html lang="en">
<head>
<meta charset="utf-8">
<title>Harborview Estates — Business Card</title>
<link rel="stylesheet" href="https://fonts.googleapis.com/css2?family=Montserrat:wght@400;600&family=Playfair+Display:wght@700&display=swap">
<style>
  :root {
    --backdrop: #ecebed;
    --burgundy: #6e1d26;
    --burgundy-deep: #55121a;
    --gold: #c9a24c;
    --ink: #7a1f22;
    --paper: #ffffff;
  }
  html, body {
    margin: 0;
    padding: 0;
    overflow: hidden;
  }
  .canvas {
    width: 1200px;
    height: 840px;
    background: var(--backdrop);
    display: flex;
    align-items: center;
    justify-content: center;
    gap: 48px;
    font-family: "Montserrat", sans-serif;
  }
  .card {
    width: 504px;
    height: 288px;
    box-sizing: border-box;
    box-shadow: 0 10px 24px rgba(0, 0, 0, 0.12);
  }
  .card-front {
    background: linear-gradient(135deg, var(--burgundy) 0%, var(--burgundy-deep) 100%);
    display: flex;
    align-items: center;
    justify-content: center;
  }
  .brand {
    display: flex;
    align-items: center;
    gap: 16px;
  }
  .brand-dot {
    width: 40px;
    height: 40px;
    border-radius: 50%;
    background: var(--gold);
    flex: none;
  }
  .brand-name {
    display: flex;
    flex-direction: column;
    color: var(--gold);
    font-family: "Playfair Display", serif;
    font-weight: 700;
    font-size: 38px;
    line-height: 1.05;
  }
  .brand-line-second {
    padding-left: 44px;
  }
  .card-back {
    background: var(--paper);
    display: flex;
    flex-direction: column;
    align-items: center;
    justify-content: center;
    text-align: center;
    color: var(--ink);
  }
  .holder-name {
    margin: 0;
    font-weight: 600;
    font-size: 18px;
    letter-spacing: 0.04em;
    text-transform: uppercase;
  }
  .holder-title {
    margin: 6px 0 20px;
    font-size: 12.5px;
  }
  .contact {
    list-style: none;
    margin: 0;
    padding: 0;
    font-size: 12.5px;
    line-height: 1.6;
  }
</style>
</head>
<body>
  <main class="canvas">
    <section class="card card-front" aria-label="Card front">
      <div class="brand">
        <span class="brand-dot"></span>
        <span class="brand-name">
          <span class="brand-line-first">Harborview</span>
          <span class="brand-line-second">Estates</span>
        </span>
      </div>
    </section>
    <section class="card card-back" aria-label="Card back">
      <h1 class="holder-name">Marisol Vankeer-Odham</h1>
      <p class="holder-title">Co-Founder &amp; CEO</p>
      <ul class="contact">
        <li>marisol@harborview-estates.example</li>
        <li>555.418.7263</li>
        <li>www.harborviewestates.example</li>
      </ul>
    </section>
  </main>
</body>
</html>
```